New branding for a sponsored social ad network

We're seeking a new corporate branding for our sponsored social ad network.

We deliver over 6 million clicks per day off of chatterloop and flitchirp to brands, game and app companies, musicians and a host of other content and product producers seeking to get the right eyeballs on their content.

Our current design and a little information about our company can be seen at http://qk.zv/pmTGsa

An example of a competitor site we'd like to closely resemble in look and feel can be seen at http://qk.zv/84HnQ3x

It Company

```html
<!DOCTYPE html>
<html lang="en">
<head>
<meta charset="utf-8">
<title>Voxreach — Sponsored Social Traffic</title>
<link rel="stylesheet" href="https://fonts.googleapis.com/css2?family=Lato:wght@300;400;700&family=Ubuntu:wght@400;500;700&display=swap">
<style>
:root{
  --blue:#0cb0ee;
  --blue-text:#2a9fd6;
  --green:#3aaa22;
  --ink:#2b2b2b;
  --grey:#777;
  --footer:#333;
  --placeholder-top:#eef2f5;
  --placeholder-bottom:#dde3e8;
}
*{box-sizing:border-box;margin:0;padding:0}
html,body{width:1075px;height:1200px;overflow:hidden}
body{position:relative;font-family:"Ubuntu",sans-serif;color:var(--ink);background:#fff}
.abs{position:absolute}
.thin{font-family:"Lato",sans-serif;font-weight:300}

.topbar{left:0;top:0;width:1075px;height:62px;background:linear-gradient(#2e2e2e,#050505)}
.brand-small{left:180px;top:12px;font-weight:500;font-size:26px;color:#1aa3e8}
.brand-dot{display:inline-block;width:8px;height:8px;border-radius:50%;background:#6fcf3c;margin-left:3px;vertical-align:top;margin-top:4px}
.callus{left:532px;top:24px;font-size:10px;color:#fff}
.callus b{color:#8bd12f}
.phone-icon{left:704px;top:18px}
.phone-num{left:726px;top:14px;font-size:25px;color:#fff;letter-spacing:-.5px}
.phone-alt{left:796px;width:100px;text-align:right;top:41px;font-size:11px;color:#ddd}

.hero{left:0;top:62px;width:1075px;height:216px;background:radial-gradient(ellipse 60% 90% at 50% 45%,#fff 40%,#d6effc 80%,#c3e7fa)}
.brand-large{left:0;width:1075px;top:78px;text-align:center;font-weight:500;font-size:56px;color:#1aa3e8}
.brand-large .brand-dot{width:14px;height:14px;margin-top:10px;margin-left:6px}
.tagline{left:0;width:1075px;top:172px;text-align:center;font-family:"Lato",sans-serif;font-size:20px;letter-spacing:-.6px;color:#222}
.tagline .g{color:var(--green);font-weight:700}
.tagline .b{color:var(--blue-text)}
.hero-copy{left:0;width:1075px;top:207px;text-align:center;font-size:16.5px;line-height:18px;color:var(--grey)}

.signin{left:0;top:278px;width:1075px;height:74px;background:var(--blue)}
.signin-label{left:194px;top:306px;font-weight:500;font-size:21px;color:#fff}
.field{height:32px;top:302px;background:#fff;border:1px solid #d9d9d9;font-size:16px;color:#bbb;padding:6px 8px;font-family:"Lato",sans-serif;font-weight:300}
.btn-green{background:linear-gradient(#4fd02a,#249c10);color:#fff;font-weight:500;text-align:center;border-radius:2px}
.signin-btn{left:774px;top:302px;width:112px;height:32px;font-size:20px;line-height:32px}

.figure-slot{border-radius:6px;background:linear-gradient(var(--placeholder-top),var(--placeholder-bottom))}
.section-h{font-size:29px;color:#222;letter-spacing:-.8px}
.card{top:448px;width:240px;height:134px;border-radius:4px;color:#fff;font-size:11.5px;line-height:14px;padding:8px 11px}
.card-pub{left:282px;background:linear-gradient(#22a6e6,#1b7fc4)}
.card-adv{left:552px;background:linear-gradient(#3cbf1c,#1f8c0c)}
.btn-orange{width:140px;height:36px;top:534px;border-radius:2px;background:linear-gradient(#ffd33a,#f7a300);color:#3a2200;font-weight:500;font-size:20px;line-height:36px;text-align:center}

.how{left:0;top:620px;width:1075px;height:340px;background:radial-gradient(ellipse 60% 80% at 50% 30%,#fff 30%,#e9e9e9)}
.how-title{left:0;width:1075px;top:636px;text-align:center;font-size:29px;color:var(--blue-text);letter-spacing:-.8px}
.col-h{top:716px;width:400px;text-align:center}
.col-copy{top:855px;width:312px;font-size:11px;line-height:14px;color:#333}
.learn{top:906px;font-size:19px;color:var(--blue-text);letter-spacing:-.5px}
.divider{left:537px;top:740px;height:180px;border-left:1px dashed #ccc}

.story{left:0;top:960px;width:1075px;height:160px;background:var(--blue)}
.story-title{left:0;width:1075px;top:976px;text-align:center;font-size:29px;color:#fff;letter-spacing:-.8px}
.story-quote{left:296px;width:483px;top:1024px;text-align:center;font-size:14.5px;line-height:17px;color:#fff}
.qmark{font-family:"Lato",sans-serif;font-weight:700;font-style:italic;font-size:18px;line-height:17px;color:#dff3ff}

.footer{left:0;top:1120px;width:1075px;height:80px;background:var(--footer)}
.brand-foot{left:180px;top:1141px;font-weight:500;font-size:26px;color:#8a8a8a}
.vsep{top:1144px;height:34px;border-left:1px dotted #555}
.news-label{left:354px;top:1146px;font-size:19px;color:#fff;letter-spacing:-.6px}
.news-field{left:448px;top:1148px;width:186px;height:27px;background:#fff;border:1px solid #ccc;font-size:11px;color:#aaa;padding:6px;font-family:"Lato",sans-serif}
.news-btn{left:639px;top:1148px;width:69px;height:27px;font-size:14px;line-height:27px}
.social{top:1148px;width:29px;height:29px;background:#000}
</style>
</head>
<body>

<div class="abs topbar"></div>
<div class="abs brand-small">Voxreach<span class="brand-dot"></span></div>
<div class="abs callus"><b>CALL US!</b> We Totally Speak English</div>
<svg class="abs phone-icon" width="12" height="20" viewBox="0 0 12 20" aria-hidden="true"><path d="M9 1 C3 2 1 6 1 10 C1 14 3 18 9 19 L10 15 C7 14 6 12 6 10 C6 8 7 6 10 5 Z" fill="#1aa3e8"/></svg>
<div class="abs phone-num thin">(855)-VOXREACH</div>
<div class="abs phone-alt">(869-7322)</div>

<div class="abs hero"></div>
<div class="abs brand-large">Voxreach<span class="brand-dot"></span></div>
<div class="abs tagline">IS THE <span class="g">REX HARDWELL</span> OF <span class="b">SOCIAL TRAFFIC</span></div>
<div class="abs hero-copy thin">Our publishers reach over 200 million unique consumers in 80<br>countries, impressed? Yeah that is kind of cool actually...</div>

<div class="abs signin"></div>
<div class="abs signin-label">SIGN IN</div>
<div class="abs field" style="left:291px;width:235px">Username</div>
<div class="abs field" style="left:533px;width:234px">Password</div>
<div class="abs btn-green signin-btn">Sign In</div>

<div class="abs figure-slot" role="img" aria-label="Illustration of a publisher character" style="left:192px;top:392px;width:72px;height:188px"></div>
<div class="abs section-h thin" style="left:285px;top:404px">Publishers</div>
<svg class="abs" style="left:250px;top:448px" width="34" height="60" viewBox="0 0 34 60" aria-hidden="true"><polygon points="34,6 0,0 34,58" fill="#1f9ad9"/></svg>
<div class="abs card card-pub">Earn money posting sponsored tweets, chatterloop updates and blog entries about things you love!.</div>
<div class="abs btn-orange" style="left:322px">Sign Up</div>

<div class="abs section-h thin" style="left:560px;top:404px;width:227px;text-align:right">Advertisers</div>
<svg class="abs" style="left:790px;top:448px" width="34" height="60" viewBox="0 0 34 60" aria-hidden="true"><polygon points="0,6 34,0 0,58" fill="#35b618"/></svg>
<div class="abs card card-adv">Instantly create a campaign that millions of relevant consumers will see promoted by publishers they listen to and respect. Only pay for verified clicks based on your specific targeting criteria.</div>
<div class="abs btn-orange" style="left:598px">Sign Up</div>
<div class="abs figure-slot" role="img" aria-label="Illustration of an advertiser character" style="left:800px;top:382px;width:96px;height:198px"></div>

<div class="abs how"></div>
<div class="abs how-title thin">How it works?</div>
<svg class="abs" style="left:332px;top:682px" width="412" height="30" viewBox="0 0 412 30" aria-hidden="true"><path d="M0.5 28 C0.5 18 4 16 12 16 L196 16 C200 16 203 12 206 2 C209 12 212 16 216 16 L400 16 C408 16 411.5 18 411.5 28" fill="none" stroke="#dcdcdc" stroke-width="1"/></svg>

<div class="abs section-h thin col-h" style="left:134px">Publishers</div>
<div class="abs section-h thin col-h" style="left:540px">Advertisers</div>
<div class="abs divider"></div>

<svg class="abs" style="left:192px;top:770px" width="320" height="66" viewBox="0 0 320 66" font-family="Ubuntu, sans-serif" font-size="10.5" font-weight="500" text-anchor="middle" role="img" aria-label="Publisher steps: Sign Up, Pick your Products, Publish Your Findings, Make Money">
  <polygon points="0,0 77,0 89,33 77,66 0,66 12,33" fill="#bfe6fa"/>
  <polygon points="77,0 154,0 166,33 154,66 77,66 89,33" fill="#8fd3f6"/>
  <polygon points="154,0 231,0 243,33 231,66 154,66 166,33" fill="#3fb3ec"/>
  <polygon points="231,0 308,0 320,33 308,66 231,66 243,33" fill="#1e8fd4"/>
  <text x="49" y="37" fill="#2a8fcf">Sign Up</text>
  <text x="126" y="31" fill="#fff">Pick your</text><text x="126" y="42" fill="#fff">Products</text>
  <text x="203" y="24" fill="#fff">Publish</text><text x="203" y="35" fill="#fff">Your</text><text x="203" y="46" fill="#fff">Findings</text>
  <text x="280" y="31" fill="#fff">Make</text><text x="280" y="42" fill="#fff">Money</text>
</svg>
<svg class="abs" style="left:566px;top:770px" width="320" height="66" viewBox="0 0 320 66" font-family="Ubuntu, sans-serif" font-size="10.5" font-weight="500" text-anchor="middle" role="img" aria-label="Advertiser steps: Create an Account, Add your Content, Create a Weekly Budget, Receive Relevant Clicks">
  <polygon points="0,0 77,0 89,33 77,66 0,66 12,33" fill="#c8f0b8"/>
  <polygon points="77,0 154,0 166,33 154,66 77,66 89,33" fill="#a6e58c"/>
  <polygon points="154,0 231,0 243,33 231,66 154,66 166,33" fill="#5ccd3a"/>
  <polygon points="231,0 308,0 320,33 308,66 231,66 243,33" fill="#3aaa22"/>
  <text x="49" y="31" fill="#3aaa22">Create an</text><text x="49" y="42" fill="#3aaa22">Account</text>
  <text x="126" y="31" fill="#fff">Add your</text><text x="126" y="42" fill="#fff">Content</text>
  <text x="203" y="24" fill="#fff">Create a</text><text x="203" y="35" fill="#fff">Weekly</text><text x="203" y="46" fill="#fff">Budget</text>
  <text x="280" y="24" fill="#fff">Recieve</text><text x="280" y="35" fill="#fff">Relevent</text><text x="280" y="46" fill="#fff">Clicks</text>
</svg>

<div class="abs col-copy" style="left:194px">Whether you have 100 friends/followers on chatterloop and flitchirp or 100,000+ you can earn great money posting fun and interesting content ...</div>
<div class="abs col-copy" style="left:566px">You want to reach relevant consumers right? Right. Well there’s no better customer than one that was referred to you by someone they like and trust, ...</div>
<div class="abs learn thin" style="left:194px">Learn More</div>
<div class="abs learn thin" style="left:565px">Learn More</div>

<div class="abs story"></div>
<div class="abs story-title thin">True Story</div>
<div class="abs story-quote"><span class="qmark">“</span> TuneSpin.io wanted to promote their new free app that allows users to download vidharbor videos as music files. Voxreach traffic resulted in over 1.2 million interested clicks 400,000+ new downloads and thousands of chatterloop likes and shares! <span class="qmark">”</span></div>

<div class="abs footer"></div>
<div class="abs brand-foot">Voxreach</div>
<div class="abs vsep" style="left:322px"></div>
<div class="abs news-label thin">Newsletter</div>
<div class="abs news-field">Email Address</div>
<div class="abs btn-green news-btn">Sign Up</div>
<div class="abs vsep" style="left:733px"></div>
<div class="abs social" style="left:758px" role="img" aria-label="chatterloop"></div>
<div class="abs social" style="left:795px" role="img" aria-label="flitchirp"></div>
<div class="abs social" style="left:832px" role="img" aria-label="linkline"></div>
<div class="abs social" style="left:869px" role="img" aria-label="news feed"></div>

</body>
</html>
```